Brinevale Yacht Management Full Page Ad Flyer

Yacht Management Package also includes the following periodic Monthly services:

Monthly full vessel systems checklist inspections
Diver For Hull Cleaning And Inspection Of Props, Shafts, and Zincs
Interior/Exterior Detailing and scheduled washdowns
Manage Haulout
Pump-out Services
On-call Captain and Crew Services
Updates

Need more time to provide more content to designers and the printing press template file.

Target Market(s)

Vessel owners, motor yachts, sailboats from 25 feet in length up to 125 feet in length. We do not do cruise ships or yachts larger than 125 feet. Someone who has their boat docked at their house or a local marina. We also offer mobile on-site services.

```html
<!DOCTYPE html>
<html lang="en">
<head>
<meta charset="utf-8">
<title>Brinevale Yacht Management Flyer</title>
<link rel="stylesheet" href="https://fonts.googleapis.com/css2?family=Outfit:wght@400;500;700;800&family=Poppins:wght@400;500;600;700&family=Oswald:wght@500;700&family=Josefin+Sans:wght@400;600&display=swap">
<style>
  :root {
    --page-bg: #e4e4e4;
    --sea-deep: #0b1d2c;
    --sea-mid: #12385a;
    --sea-light: #1c5f8f;
    --accent: #1598f0;
    --accent-soft: #3d7ff0;
    --white: #ffffff;
    --badge-top: #f78a1c;
    --badge-bottom: #e8101a;
  }
  * { margin: 0; padding: 0; box-sizing: border-box; }
  html, body { width: 1200px; height: 1200px; overflow: hidden; background: var(--page-bg); }
  .flyer {
    position: absolute; left: 136px; top: 0; width: 927px; height: 1200px;
    overflow: hidden; color: var(--white); font-family: "Poppins", sans-serif;
  }
  .flyer__photo {
    position: absolute; inset: 0;
    background:
      radial-gradient(ellipse 420px 760px at 82% 78%, rgba(170,190,205,.45), transparent 70%),
      radial-gradient(ellipse 560px 520px at 95% 10%, var(--sea-light), transparent 75%),
      linear-gradient(160deg, var(--sea-mid) 0%, var(--sea-deep) 55%, #0d2233 100%);
  }
  .headline { position: absolute; left: 72px; top: 52px; }
  .headline__top {
    font-family: "Outfit", sans-serif; font-weight: 800; font-size: 96px;
    line-height: 1; color: var(--accent); letter-spacing: -1px;
  }
  .headline__bottom {
    font-family: "Josefin Sans", sans-serif; font-weight: 600; font-size: 94px;
    line-height: 1; margin-top: 6px; letter-spacing: -1px;
  }
  .divider { position: absolute; left: 84px; top: 249px; display: flex; gap: 6px; }
  .divider span { width: 16px; height: 14px; background: var(--accent); }
  .divider span:nth-child(2) { opacity: .85; }
  .divider span:nth-child(3) { opacity: .65; }
  .divider span:nth-child(4) { opacity: .45; }
  .divider span:nth-child(5) { opacity: .25; }
  .intro {
    position: absolute; left: 83px; top: 292px; width: 480px;
    font-family: "Josefin Sans", sans-serif; font-weight: 400; font-size: 23px;
    line-height: 1.2; text-transform: uppercase;
  }
  .intro__highlight {
    display: block; margin-top: 8px; font-family: "Outfit", sans-serif;
    font-weight: 700; font-size: 26px; color: var(--accent);
  }
  .services { position: absolute; left: 84px; top: 414px; list-style: none; }
  .services__item {
    position: absolute; left: 0; width: 460px; padding-left: 31px;
    font-size: 20px; line-height: 23px;
  }
  .services__tick { position: absolute; left: 0; top: 2px; width: 16px; height: 16px; }
  .brand {
    position: absolute; left: 84px; top: 820px;
    font-family: "Poppins", sans-serif; font-weight: 400; font-size: 34px;
    letter-spacing: 7px; text-transform: uppercase;
  }
  .cta { position: absolute; left: 84px; top: 893px; }
  .cta__lead { font-size: 28px; font-weight: 500; line-height: 1.2; }
  .cta__main {
    font-family: "Outfit", sans-serif; font-weight: 700; font-size: 40px;
    color: var(--accent); line-height: 1.1; letter-spacing: .5px;
  }
  .contact { position: absolute; left: 84px; }
  .contact__icon { position: absolute; left: 0; width: 34px; height: 34px; }
  .contact--phone { top: 991px; }
  .contact--phone .contact__text { position: absolute; left: 49px; top: -1px; font-size: 27px; white-space: nowrap; }
  .contact--place { top: 1041px; }
  .contact--place .contact__text { position: absolute; left: 49px; top: -6px; white-space: nowrap; font-size: 20px; line-height: 1.25; }
  .contact__label { color: var(--accent-soft); font-weight: 600; }
  .website {
    position: absolute; left: 84px; top: 1106px;
    font-size: 26px; letter-spacing: 5px;
  }
  .website__name { color: var(--accent); font-weight: 600; }
  .badge { position: absolute; left: 530px; top: 301px; width: 230px; height: 230px; }
  .badge__text {
    position: absolute; inset: 0; display: flex; flex-direction: column;
    align-items: center; justify-content: center; text-align: center; padding-top: 4px;
  }
  .badge__small { font-family: "Oswald", sans-serif; font-weight: 500; font-size: 29px; line-height: 1; }
  .badge__big { font-family: "Oswald", sans-serif; font-weight: 700; font-size: 60px; line-height: 1; margin-top: 2px; }
  .badge__note { font-family: "Poppins", sans-serif; font-weight: 700; font-size: 14px; line-height: 1.3; margin-top: 4px; }
</style>
</head>
<body>
<main class="flyer">
  <div class="flyer__photo" role="img" aria-label="Aerial photo of open blue ocean with a wooden speedboat leaving a white wake"></div>

  <h1 class="headline">
    <div class="headline__top">YACHT</div>
    <div class="headline__bottom">MANAGEMENT</div>
  </h1>

  <div class="divider"><span></span><span></span><span></span><span></span><span></span></div>

  <p class="intro">Yacht management package also includes the following
    <span class="intro__highlight">Periodic Monthly Services</span>
  </p>

  <ul class="services">
    <li class="services__item" style="top:2px"><svg class="services__tick" viewBox="0 0 16 16"><rect width="16" height="16" rx="3" fill="#1598f0"/><path d="M4 8.2l2.7 2.6L12 5.4" fill="none" stroke="#0b1d2c" stroke-width="2"/></svg>Monthly full vessel systems<br>checklist inspections</li>
    <li class="services__item" style="top:70px"><svg class="services__tick" viewBox="0 0 16 16"><rect width="16" height="16" rx="3" fill="#1598f0"/><path d="M4 8.2l2.7 2.6L12 5.4" fill="none" stroke="#0b1d2c" stroke-width="2"/></svg>Diver For Hull Cleaning And Inspection<br>Of Props, Shafts, and Zincs</li>
    <li class="services__item" style="top:138px"><svg class="services__tick" viewBox="0 0 16 16"><rect width="16" height="16" rx="3" fill="#1598f0"/><path d="M4 8.2l2.7 2.6L12 5.4" fill="none" stroke="#0b1d2c" stroke-width="2"/></svg>Interior/Exterior Detailing and<br>scheduled washdowns</li>
    <li class="services__item" style="top:206px"><svg class="services__tick" viewBox="0 0 16 16"><rect width="16" height="16" rx="3" fill="#1598f0"/><path d="M4 8.2l2.7 2.6L12 5.4" fill="none" stroke="#0b1d2c" stroke-width="2"/></svg>Manage Haulout</li>
    <li class="services__item" style="top:252px"><svg class="services__tick" viewBox="0 0 16 16"><rect width="16" height="16" rx="3" fill="#1598f0"/><path d="M4 8.2l2.7 2.6L12 5.4" fill="none" stroke="#0b1d2c" stroke-width="2"/></svg>Pump-out Services</li>
    <li class="services__item" style="top:298px"><svg class="services__tick" viewBox="0 0 16 16"><rect width="16" height="16" rx="3" fill="#1598f0"/><path d="M4 8.2l2.7 2.6L12 5.4" fill="none" stroke="#0b1d2c" stroke-width="2"/></svg>On-call Captain and<br>Crew Services</li>
  </ul>

  <div class="brand">Brinevale</div>

  <div class="cta">
    <p class="cta__lead">Call Today for a</p>
    <p class="cta__main">FREE ESTIMATE</p>
  </div>

  <div class="contact contact--phone">
    <svg class="contact__icon" viewBox="0 0 34 34"><circle cx="17" cy="17" r="17" fill="#1598f0"/><path d="M12.5 9.5l2.6 3.4-1.6 2c.9 2 2.4 3.6 4.5 4.6l2-1.6 3.4 2.6-1.6 2.8c-5.6-.3-11-5.8-11.3-11.3z" fill="#0b1d2c"/></svg>
    <span class="contact__text">012.555.0147</span>
  </div>

  <div class="contact contact--place">
    <svg class="contact__icon" viewBox="0 0 34 34"><circle cx="17" cy="17" r="17" fill="#1598f0"/><path d="M17 7.5a6.5 6.5 0 0 0-6.5 6.5c0 4.8 6.5 12 6.5 12s6.5-7.2 6.5-12A6.5 6.5 0 0 0 17 7.5z" fill="#0b1d2c"/><circle cx="17" cy="14" r="2.4" fill="#1598f0"/></svg>
    <p class="contact__text"><span class="contact__label">Located in</span><br>South Florida Miami area</p>
  </div>

  <p class="website">www.<span class="website__name">brinevale</span>.com</p>

  <div class="badge">
    <svg viewBox="-120 -120 240 240" width="230" height="230">
      <defs>
        <linearGradient id="badgeFill" x1="0" y1="0" x2="0" y2="1">
          <stop offset="0" stop-color="#f78a1c"/>
          <stop offset="1" stop-color="#e8101a"/>
        </linearGradient>
      </defs>
      <polygon fill="url(#badgeFill)" stroke="url(#badgeFill)" stroke-width="14" stroke-linejoin="round"
        points="104,0 88.9,23.8 90.1,52 65,65 52,90.1 23.8,88.9 0,104 -23.8,88.9 -52,90.1 -65,65 -90.1,52 -88.9,23.8 -104,0 -88.9,-23.8 -90.1,-52 -65,-65 -52,-90.1 -23.8,-88.9 0,-104 23.8,-88.9 52,-90.1 65,-65 90.1,-52 88.9,-23.8"/>
      <circle r="88" fill="none" stroke="#ffffff" stroke-width="1.5" stroke-dasharray="5 4"/>
    </svg>
    <div class="badge__text">
      <span class="badge__small">WE ALSO</span>
      <span class="badge__big">OFFER</span>
      <span class="badge__note">MOBILE ON-SITE<br>SERVICES</span>
    </div>
  </div>
</main>
</body>
</html>
```